Consultant Firm Marketing Flyer

I want to use this flyer to market health care consultant services. I would like a front and back glossy, professional, yet bold and eye catching design. I would like it to convey knowledge, expertise, partnership and strength. The colors should blue and white but I am very open to the designer being creative. You can visit my website to see colors and images I want to use at brightmeadowadvisory.com
I would like the home page image on my website to be incorporated into the flyer but I am also open to other images that work with the design. The designer can be creative.

I want to highlight 4 service area’s of focus to my clients:
1. Revenue Cycle Optimization (making my clients money)
2. Practice Management Optimization (improving clinical operations)
3. Health Compliance (following the law)
4. Health Care Technology: (Telemedicine and AI)
Please be creative. Go where ever your creativity leads.

```html
<!DOCTYPE html>
<html lang="en">
<head>
<meta charset="utf-8">
<title>Bright Meadow Advisory – Flyer</title>
<link href="https://fonts.googleapis.com/css2?family=Roboto+Slab:wght@300;400;500&display=swap" rel="stylesheet">
<style>
  :root {
    --stage: #9b9b9b;
    --sky: #cfe6ea;
    --sky-deep: #a9d3da;
    --blue: #34a3d8;
    --blue-dark: #1c6e96;
    --teal-text: #2a8a93;
    --ink: #1f3f4a;
    --navy: #1e4f8f;
    --panel: rgba(255,255,255,0.5);
    --glow: rgba(255,255,255,0.22);
    --glow-soft: rgba(255,255,255,0.08);
  }
  * { margin: 0; padding: 0; box-sizing: border-box; }
  html, body { width: 1200px; height: 1200px; overflow: hidden; background: var(--stage); }
  body { font-family: "Roboto Slab", Georgia, serif; position: relative; }

  .spread { position: absolute; left: 59px; top: 234px; width: 1352px; height: 915px; transform: scale(0.8); transform-origin: 0 0; }
  .page { position: absolute; top: 0; width: 665px; height: 915px; overflow: hidden;
    background: linear-gradient(160deg, var(--sky) 0%, var(--sky-deep) 55%, var(--sky) 100%); }
  .page--front { left: 0; }
  .page--back { left: 687px; }

  .bokeh { position: absolute; inset: 0; pointer-events: none;
    background:
      radial-gradient(circle at 12% 5%, var(--glow) 0, var(--glow-soft) 30px, transparent 46px),
      radial-gradient(circle at 38% 3%, var(--glow) 0, var(--glow-soft) 24px, transparent 38px),
      radial-gradient(circle at 62% 6%, var(--glow) 0, var(--glow-soft) 28px, transparent 44px),
      radial-gradient(circle at 88% 4%, var(--glow) 0, var(--glow-soft) 30px, transparent 48px),
      radial-gradient(circle at 8% 70%, var(--glow-soft) 0, var(--glow-soft) 40px, transparent 60px),
      radial-gradient(circle at 50% 80%, var(--glow-soft) 0, var(--glow-soft) 45px, transparent 66px),
      radial-gradient(circle at 92% 72%, var(--glow-soft) 0, var(--glow-soft) 40px, transparent 60px),
      radial-gradient(circle at 30% 96%, var(--glow-soft) 0, var(--glow-soft) 34px, transparent 52px),
      radial-gradient(circle at 80% 97%, var(--glow-soft) 0, var(--glow-soft) 34px, transparent 52px);
  }
  .page > *:not(.bokeh) { z-index: 1; }
  .page svg.shapes { position: absolute; left: 0; top: 0; }

  /* front */
  .hero-photo { position: absolute; left: 0; top: 87px; width: 665px; height: 470px;
    background: linear-gradient(100deg, #dfe6e8 0%, #f4f6f7 45%, #e9eef0 70%, #cfd9dd 100%); }
  .why { position: absolute; left: 22px; top: 586px; font-size: 25px; font-weight: 400; color: var(--ink); }
  .why-copy { position: absolute; left: 22px; top: 625px; width: 630px; font-size: 14px; line-height: 26.7px; font-weight: 300; color: var(--teal-text); }
  .why-copy span { display: block; white-space: nowrap; }
  .brand { position: absolute; left: 22px; top: 830px; }
  .brand-name { font-size: 26px; font-weight: 500; color: var(--navy); letter-spacing: .5px; }
  .brand-legal { font-size: 13px; color: var(--ink); letter-spacing: .6px; margin-top: 6px; }
  .contact { position: absolute; left: 321px; top: 856px; font-size: 14px; color: var(--ink); line-height: 26px; }
  .contact-row { display: flex; align-items: center; gap: 6px; }
  .social { position: absolute; left: 581px; top: 883px; display: flex; gap: 4px; }
  .social span { width: 21px; height: 21px; border-radius: 50%; background: var(--blue-dark); }
  .footer-bar { position: absolute; left: 0; bottom: 0; width: 298px; height: 12px; background: var(--blue); }

  /* back */
  .services-title { position: absolute; left: 195px; top: 14px; width: 290px; text-align: center; font-size: 30px; color: #fff; font-weight: 400; }
  .service { position: absolute; border-radius: 28px; background: var(--panel); padding: 0 14px; }
  .service-tag { margin: 14px auto 10px; width: 212px; padding: 4px 0; text-align: center; color: #fff;
    font-size: 15px; line-height: 17px; font-weight: 400; background: linear-gradient(90deg, #36b3d3, #1fa6c9, #4cc0db); border-radius: 3px; text-transform: uppercase; }
  .service p { font-size: 10px; line-height: 14px; color: var(--teal-text); font-weight: 400; margin-bottom: 6px; }
  .service ul { list-style: none; margin-bottom: 8px; }
  .service li { font-size: 10px; line-height: 14px; color: var(--ink); padding-left: 8px; text-indent: -7px; }
  .service li::before { content: "• "; }
  .s-revenue { left: 48px; top: 65px; width: 272px; height: 363px; }
  .s-compliance { left: 360px; top: 62px; width: 273px; height: 543px; }
  .s-hr { left: 46px; top: 457px; width: 274px; height: 381px; }
  .s-practice { left: 351px; top: 633px; width: 274px; height: 262px; }
  .s-practice p, .s-practice li { font-size: 9px; line-height: 13px; }
  .back-brand { position: absolute; left: 68px; top: 845px; text-align: center; width: 200px; }
  .back-brand .brand-name { font-size: 22px; }
  .back-brand .brand-legal { font-size: 11.5px; }
</style>
</head>
<body>
<div class="spread">

  <section class="page page--front">
    <div class="bokeh" aria-hidden="true"></div>
    <div class="hero-photo" role="img" aria-label="Photo of a smiling physician in a white coat with stethoscope holding a clipboard in a bright clinic"></div>
    <svg class="shapes" width="665" height="915" viewBox="0 0 665 915" aria-hidden="true">
      <polygon points="0,35 195,35 0,325" fill="#34a3d8"/>
      <polygon points="160,87 195,35 230,87" fill="#1c6e96"/>
      <polygon points="665,260 665,610 432,610" fill="#34a3d8"/>
      <polygon points="432,557 468,557 432,610" fill="#1c6e96"/>
    </svg>
    <h2 class="why">Why Choose Us</h2>
    <p class="why-copy">
      <span>Bright Meadow Advisory (BMA), founded in 2015, is a healthcare consulting</span>
      <span>firm skilled at helping physician practices advance their strategic vision in an</span>
      <span>ever-evolving healthcare system. Bright Meadow Advisory specializes in</span>
      <span>revenue cycle optimization, practice management improvement and developing</span>
      <span>new physician practices. Our technical skills allow us to dig deep into your revenue</span>
      <span>cycle while our strategic approach ensures we’re keeping our eyes on the entire</span>
      <span>financial picture.</span>
    </p>
    <div class="brand">
      <div class="brand-name">BRIGHT MEADOW</div>
      <div class="brand-legal">Bright Meadow Advisory LLC</div>
    </div>
    <div class="contact">
      <div class="contact-row">
        <svg width="18" height="16" viewBox="0 0 18 16"><path d="M4 1 L7 4 L5 6 Q7 10 11 11 L13 9 L16 12 L14 15 Q4 14 2 3 Z" fill="none" stroke="#1f3f4a" stroke-width="1.2"/></svg>
        (555) 014-2276
      </div>
      <div class="contact-row">
        <svg width="18" height="14" viewBox="0 0 18 14"><rect x="1" y="2" width="16" height="10" fill="none" stroke="#1f3f4a" stroke-width="1.2"/><path d="M1 2 L9 8 L17 2" fill="none" stroke="#1f3f4a" stroke-width="1.2"/></svg>
        Info@brightmeadowadvisory.com
      </div>
    </div>
    <div class="social" aria-hidden="true"><span></span><span></span><span></span></div>
    <div class="footer-bar"></div>
  </section>

  <section class="page page--back">
    <div class="bokeh" aria-hidden="true"></div>
    <svg class="shapes" width="665" height="915" viewBox="0 0 665 915" aria-hidden="true">
      <polygon points="196,16 470,16 470,60 183,60" fill="#1fa3c9"/>
      <polygon points="183,16 220,16 183,50" fill="#16779c"/>
      <polygon points="470,16 496,16 496,62 470,60" fill="#16779c"/>
    </svg>
    <h2 class="services-title">Our Services</h2>

    <article class="service s-revenue">
      <h3 class="service-tag">Revenue Cycle<br>Management</h3>
      <p>In today’s increasingly complex health care environment it’s important now more than ever that medical practices closely manage their revenue cycle. Bright Meadow Advisory (BMA) understands the reimbursement landscape and is skilled in helping medical practices maximize reimbursement. We offer a comprehensive package of revenue cycle services including:</p>
      <ul>
        <li>Medical Billing &amp; Coding</li>
        <li>Documentation &amp; Coding Audit</li>
        <li>A/R Management</li>
        <li>Dedicated Remote Billing Manager</li>
        <li>Dedicated Phone Number for Patients to Call</li>
        <li>Revenue Cycle Training for Practice Staff</li>
        <li>Monthly Reports</li>
        <li>Patient Access Assessment &amp; Optimization</li>
      </ul>
      <p>We offer each of these services individually or as part of a comprehensive bundled package</p>
    </article>

    <article class="service s-compliance">
      <h3 class="service-tag">Regulatory<br>Compliance</h3>
      <p>In a heavily regulated healthcare environment medical practices need to be acutely aware of regulations as they present huge liabilities. It is extremely important to ensure compliance with regulations including:</p>
      <ul>
        <li>Medical Coding Regulations</li>
        <li>False Claims Act</li>
        <li>HIPAA Privacy &amp; Security Rules</li>
        <li>Emergency Medical Treatment and Active Labor Act (EMTALA)</li>
        <li>Stark Law &amp; Anti-Kickback Statute</li>
        <li>Occupational Safety &amp; Health Administration Guidelines (OSHA)</li>
      </ul>
      <p>BMA offers a host of comprehensive compliance services. Practices have the option of completely outsourcing all compliance matters. BMA will become your full service compliance department providing:</p>
      <ul>
        <li>A Dedicated Compliance Officer</li>
        <li>Dedicated Hotline &amp; Email for Compliance Reporting</li>
        <li>Annual Work Plan &amp; Risk Assessment</li>
        <li>Compliance Training</li>
        <li>Medical Documentation Audits</li>
        <li>Compliance Plan</li>
        <li>Compliance with Safety Procedures</li>
        <li>Staff Training</li>
      </ul>
      <p>We offer each of these services individually or as part of a comprehensive bundled package. We can craft a customized package for your company. Contact us to get started</p>
    </article>

    <article class="service s-hr">
      <h3 class="service-tag">Human Resource<br>Management</h3>
      <p>Do you need Human Resources Management but don’t want the expense of a full service Human Resources Department?</p>
      <p>Not having a full service Human Resources Department can increase liability and be costly to your medical practice. Let BMA become your full service HR Department. Our Services include:</p>
      <ul>
        <li>A dedicated HR Manager</li>
        <li>Development of HR Policies and Procedures</li>
        <li>Employer Coaching and Guidance</li>
        <li>Assistance with Onboarding &amp; Terminations</li>
        <li>Compensation Compliance</li>
        <li>Navigation of Complex Labor Laws Staff Training</li>
        <li>Staff Recruitment &amp; Talent Acquisition</li>
        <li>Pre-hire background checks</li>
        <li>Compliance Services: Affirmative Action, Fair labor Standards Act (FLSA) Compliance audit, FMLA &amp; Much More.</li>
      </ul>
      <p>These services can be purchased individually or as part of a comprehensive package.</p>
    </article>

    <article class="service s-practice">
      <h3 class="service-tag">Practice<br>Management</h3>
      <p>Practice Management is challenging and it requires the right balance of skill, knowledge, experience and management expertise. BMA Offers assessment and optimization in the following areas:</p>
      <ul>
        <li>Patient Access &amp; Scheduling</li>
        <li>Patient Experience</li>
        <li>Staff Experience</li>
        <li>Online Reputation Management</li>
        <li>Strategic Planning</li>
      </ul>
      <p>We offer each of these services individually or as part of a comprehensive bundled package.</p>
    </article>

    <div class="back-brand">
      <div class="brand-name">BRIGHT MEADOW</div>
      <div class="brand-legal">Bright Meadow Advisory LLC</div>
    </div>
  </section>

</div>
</body>
</html>
```